Wordpress Frontpage/Theme redesign with Female Touch

We’d like to get a new Wordpress theme or childtheme to refresh our beloved website: ladiesinventure.com.au which is a customized version of theme ‘Plume’ that we now find a bit “childish” “chaotic” “unprofessional looking”. We are after a more clear and refined, more professionally looking site.

We’d like to use our current plugins, somebody just needs to redesign the frontpage to give us a new and awesome outlook. We can install and finetune all the necessary plugins.
We know exactly what elements we want to see on the website, see detailed Design requirements. Please also feel free to use any images from http://ladiesinventure.com.au/category/Gallery/ or other stock images.

What we like:
We’d like to have a more professional look, we like ‘news sites’ that: feminine, intelligent, exclusive, smart, elegant, confident aiming towards the higher end of the female entrepreneur market. Websites like:
http://www.gardenmorrow.com/
http://www.velvora.com/velvora/
http://thelattice.quorvix.com.au/
http://brightpeltavo.com/
http://layoutmarket.net/item/pagevane-flat-magazine-theme-/full_screen_preview/4917362

Project Deadline Extended
Reason: Hi guys, We are extending the deadline of the project as we are still waiting for the perfect design. Good luck everyone! Cheers

Target Market(s)

Australian national community of like-minded aspiring and accomplished female entrepreneurs. Age women in their 30’s and 40’s – typically confident and established powerful and driven, passionate women.

Requirements
Must have
• Detailed Design Requirements
• Read together with “Ladies in Venture website screenshot with numbers.jpg”:
• 1. Logo: New Logo provided + we need the tagline with nice characters
• 2. Social Media Buttons should be in the Footer: Chirplet, Facenook, Pinboardly, Workcircle, Feed
• 3. Drop down Menu (Multi level) JOIN menu highlighted
• 4. Picture slideshow where we can put our photos, adds, event pictures, happy women faces etc.
• 5. Search with Search button
• 6. Space which is easy to edit and where we can quickly write news, or important information
• 7. Widget: News Letter Signup (Should be highlighted and well visible)
• 8. Widget: Login with standard Facenook login button (Unikey plugin) this can be at top row header
• 9. Widget: Question of the week, Online poll
• 10. Widget: Upcoming events, Gatherly widget
• 11. Featured Video Display: 2 videos which are in the “featured videos” category, (photo + excerpt)
• 12. Featured Blog Display: Displaying blog entries which are in the “featured blogs” category (photo + excerpt)
• 13. Widgets Standard Wordpress widgets to show recent activities (can be different)
• 14. Same as 13.
• 15. Same as 13.
• 16. Same as 13.
• 17. Facenook News Feed
• 18. Footer: Social media buttons see no.2., + credit, etc..
• .
• + New features we need:
• 19. Featured members (displaying Level2 users from Q7 Roster Plugin)
• 20. Promo Viddora Video: fix space on the top somewhere, picture provided.
• 21. Place for advertisements
• Other requirements:
• • Speed: Please don’t create huge background images/javascript files, current Frontpage is ~600KB.
• • Security: no hidden codes, no well known vulnerabilities.
• • Compatibility: please use standard Wordpress features. Later on we want to add more features like: Webshop, Palpanel
• • Resizable: When we change window size, or see it on mobile, it rearranges itself.

```html
<!DOCTYPE html>
<html lang="en">
<head>
<meta charset="utf-8">
<title>Ladies in Venture</title>
<link href="https://fonts.googleapis.com/css2?family=Arimo:wght@400;700&display=swap" rel="stylesheet">
<style>
:root{
  --magenta:#e5177b;
  --red:#d8262e;
  --red-dark:#b81d24;
  --yellow:#f6c21c;
  --nav:#4b4b4b;
  --nav-dark:#3a3a3a;
  --text:#333;
  --muted:#777;
  --line:#e3e3e3;
  --panel:#f1f1f1;
  --bar:#e9e9e9;
  --footer:#454545;
  --fb:#3b5998;
}
*{box-sizing:border-box;margin:0;padding:0}
html,body{width:1200px;height:4027px;overflow:hidden}
body{background:#fff;font-family:"Arimo",Arial,sans-serif;color:var(--text);font-size:11px}
.page{width:870px;margin:0 auto;position:relative;height:4027px}
.masthead{height:118px;display:flex;align-items:center;justify-content:space-between;padding:0 4px}
.brand{font-size:52px;font-weight:700;color:var(--magenta);letter-spacing:-1px}
.brand-square{width:86px;height:86px;background:var(--magenta);border-radius:4px}
.nav{height:43px;background:var(--nav);display:flex}
.nav a{color:#fff;text-decoration:none;font-size:14px;padding:0 22px;line-height:43px;border-right:1px solid var(--nav-dark)}
.nav a.join{background:var(--magenta)}
.nav .caret{font-size:9px;margin-left:4px}
.nav .spacer{flex:1}
.hero{height:390px;position:relative;background:linear-gradient(100deg,#6a5648 0%,#b89b84 32%,#8a7565 55%,#4b4038 100%)}
.hero-copy{position:absolute;right:40px;top:150px;color:#fff}
.hero-copy .small{font-size:24px}
.hero-copy .big{font-size:34px;margin-top:6px}
.hero-arrows{position:absolute;right:10px;bottom:10px;display:flex;gap:3px}
.hero-arrows span{width:22px;height:22px;background:var(--red);color:#fff;font-size:13px;text-align:center;line-height:22px}
.body{display:flex;gap:30px}
.main{width:570px}
.side{width:270px;padding-top:22px}
.intro{text-align:center;padding-top:27px;height:245px}
.intro-brand{display:inline-flex;align-items:center;gap:10px;font-size:26px;font-weight:700;color:var(--magenta);height:81px}
.intro-brand i{width:22px;height:22px;border-radius:50%;background:var(--magenta)}
.intro h2{color:var(--magenta);font-size:15px;font-weight:400;line-height:21px;margin:21px 20px 10px;text-transform:uppercase}
.intro p{color:var(--magenta);font-size:15px}
.section-bar{height:27px;background:var(--bar);font-size:12px;font-weight:700;line-height:27px;padding-left:10px;text-transform:uppercase;color:#444}
.post{display:flex;gap:22px;height:183px;padding-top:32px;border-bottom:1px solid var(--line)}
.post:last-of-type{border-bottom:none}
.thumb{width:220px;height:132px;flex:none}
.post h3{font-size:14px;font-weight:400;color:#222;margin:4px 0 10px}
.post .date{color:var(--red);font-size:11px;margin-bottom:8px}
.post p{font-size:11px;line-height:18px;color:#555}
.articles .post{height:186px;padding-top:24px}
.articles .thumb{height:162px}
.more{display:flex;justify-content:flex-end;padding:6px 0}
.more span{background:#555;color:#fff;font-size:12px;padding:0 20px;line-height:28px;border-radius:3px}
.ad-banner{margin:20px auto 30px;width:410px;height:54px;background:linear-gradient(90deg,#2e4d8f,#5f7fc0);display:flex;align-items:center;justify-content:space-between;padding:0 16px;color:#fff;font-size:17px;font-weight:700}
.ad-banner small{font-size:11px;font-weight:400;background:var(--red);padding:6px 10px}
.feed{margin-top:16px;height:403px;border:1px solid #ccc;padding:14px}
.feed-head{display:flex;gap:12px;align-items:center;font-size:13px;font-weight:700;color:var(--fb)}
.feed-head i{width:40px;height:40px;background:var(--magenta)}
.feed-head .like{font-size:10px;background:#f0f0f0;border:1px solid #ccc;color:#333;padding:2px 6px;font-weight:400;margin-top:4px;display:inline-block}
.feed-photo{height:44px;margin:8px 0 0 52px;background:linear-gradient(#d7c2e8,#b38fd3)}
.feed-meta{font-size:10px;color:var(--muted);margin:6px 0 12px 52px}
.feed p{font-size:12px;line-height:16px;margin-left:52px}
.feed-quote{height:78px;margin:8px 0 0 52px;background:linear-gradient(90deg,#e9e0d6,#c9b7a6)}
.feed-fans{font-size:11px;margin:12px 0 6px}
.feed-fans b{color:var(--fb)}
.fan-grid{height:62px;background:linear-gradient(90deg,#9c8a7c,#cdb9a8,#8f7f72)}
.feed-foot{font-size:10px;color:var(--muted);margin-top:6px}
.side-label{color:var(--red);font-size:13px;font-weight:700;text-transform:uppercase;margin-bottom:8px}
.search{display:flex;gap:6px;margin-bottom:22px}
.search .field{flex:1;height:32px;border:1px solid #bbb}
.search .btn{width:70px;background:#555;color:#fff;font-size:12px;text-align:center;line-height:32px;border-radius:3px}
.newsletter{background:var(--red);height:172px;padding:14px;color:#fff}
.newsletter h4{font-size:12px;text-transform:uppercase;margin-bottom:10px}
.newsletter .field{height:30px;background:#fff;color:#999;font-size:11px;line-height:30px;padding-left:8px;margin-bottom:8px}
.newsletter .signup{height:34px;background:var(--yellow);color:var(--red-dark);font-size:16px;text-align:center;line-height:34px;margin-top:4px}
.widget{background:var(--panel);padding:14px;margin-top:28px}
.widget h4{color:var(--red);font-size:12px;text-transform:uppercase;margin-bottom:12px}
.login{height:173px;text-align:center}
.btn-row{display:flex;justify-content:center;gap:8px;margin-bottom:12px}
.btn-row span,.poll-btns span{background:#555;color:#fff;font-size:12px;padding:0 16px;line-height:28px;border-radius:3px}
.login p{font-size:12px;color:#555;margin-bottom:12px}
.fb-connect{display:inline-block;background:var(--fb);color:#fff;font-size:11px;padding:0 14px;line-height:26px;border-radius:3px}
.poll{height:210px;margin-top:26px}
.poll .q{font-size:12px;margin-bottom:8px}
.poll label{display:flex;gap:6px;font-size:10px;color:#555;line-height:13px;margin-bottom:7px}
.poll label i{width:10px;height:10px;border:1px solid #999;border-radius:50%;background:#fff;flex:none;margin-top:1px}
.poll .vote{font-size:10px;color:var(--red);text-decoration:underline;margin:2px 0 6px}
.poll-btns{display:flex;gap:8px}
.side-ad{height:215px;margin-top:113px;background:linear-gradient(135deg,#2f8a2f,#8ac43f);padding:14px;color:#fff}
.side-ad b{display:block;font-size:30px;line-height:30px}
.side-ad span{display:block;margin-top:100px;background:var(--red);font-size:12px;padding:4px 6px}
.events{height:436px;margin-top:22px}
.event{display:flex;gap:10px;margin-bottom:14px}
.event .title{font-size:11px;margin-bottom:6px;color:#333}
.event .pic{width:70px;height:56px;flex:none;background:linear-gradient(#5a4b45,#a08a7c)}
.event p{font-size:10px;line-height:14px;color:#666}
.events .more{padding:2px 0}
.list{background:#fff;padding:0;margin-top:30px}
.list h4{background:var(--panel);color:#444;font-size:12px;line-height:28px;padding-left:10px;margin-bottom:4px}
.list li{list-style:none;font-size:10px;color:#555;line-height:20.5px;border-bottom:1px solid var(--line);padding-left:10px;position:relative}
.list li::before{content:"";position:absolute;left:2px;top:9px;width:3px;height:3px;background:#999}
.list.archives li{line-height:20.3px}
.ad2{height:215px;margin-top:26px;background:linear-gradient(135deg,#3a9b3a,#a6d86a);padding:14px;color:#fff}
.ad2 b{display:block;font-size:20px;line-height:24px}
.ad2 span{display:block;margin-top:70px;font-size:18px;font-weight:700}
.footer{position:absolute;left:0;right:0;top:3887px;height:90px;background:var(--footer);display:flex;align-items:center;justify-content:space-between;padding:0 22px;color:#ccc;font-size:11px}
.social{display:flex;gap:12px}
.social span{display:flex;align-items:center;gap:4px;font-size:10px;color:#ccc}
.social i{width:16px;height:16px;border-radius:50%;background:#666}
</style>
</head>
<body>
<div class="page">
  <header class="masthead">
    <div class="brand">Ladies in Venture</div>
    <div class="brand-square"></div>
  </header>
  <nav class="nav">
    <a>Home</a><a>About<span class="caret">▼</span></a><a>Events</a><a>Resources<span class="caret">▼</span></a><a>Biz Directory<span class="caret">▼</span></a><a class="join">Join</a><a>Partners</a><span class="spacer"></span><a>Contact</a>
  </nav>
  <section class="hero" role="img" aria-label="Slideshow photo of a smiling female entrepreneur">
    <div class="hero-copy"><div class="small">Australia's No.1organisation for</div><div class="big">Female entrepreneurs</div></div>
    <div class="hero-arrows"><span>‹</span><span>›</span></div>
  </section>

  <div class="body">
    <main class="main">
      <div class="intro">
        <div class="intro-brand"><i></i>Ladies in Venture</div>
        <h2>We provide women entrepreneurs with information, support and a community in Australia.</h2>
        <p>Do what you love • Inspire others • Change the world</p>
      </div>

      <div class="section-bar">Featured Videos</div>
      <section class="videos">
        <article class="post"><div class="thumb" role="img" aria-label="Video still of illustrated people" style="background:linear-gradient(135deg,#3aa6e0,#7fd0f2)"></div><div><h3>Ladies in Venture Testimonial Video</h3><div class="date">Mira Halloway, March 6, 2013</div><p>Ladies in Venture (LV) is the No 1 community for Australian female entrepreneurs, run by Mira Halloway and focuses on empowerment of women and equal opportunity advocacy.</p></div></article>
        <article class="post"><div class="thumb" role="img" aria-label="Video still of a speaker" style="background:linear-gradient(135deg,#5d5450,#a99a90)"></div><div><h3>Ladies in Venture Testimonial Video</h3><div class="date">Mira Halloway, March 6, 2013</div><p>Ladies in Venture (LV) is the No 1 community for Australian female entrepreneurs, run by Mira Halloway and focuses on empowerment of women and equal opportunity advocacy.</p></div></article>
        <article class="post"><div class="thumb" role="img" aria-label="Video still of members at an event" style="background:linear-gradient(135deg,#2e2624,#8a6f60)"></div><div><h3>Ladies in Venture Testimonial Video</h3><div class="date">Mira Halloway, March 6, 2013</div><p>Ladies in Venture (LV) is the No 1 community for Australian female entrepreneurs, run by Mira Halloway and focuses on empowerment of women and equal opportunity advocacy.</p></div></article>
        <article class="post"><div class="thumb" role="img" aria-label="Video still of women posing" style="background:linear-gradient(135deg,#d9d0c8,#8c6a5c)"></div><div><h3>Ladies in Venture Testimonial Video</h3><div class="date">Mira Halloway, March 6, 2013</div><p>Ladies in Venture (LV) is the No 1 community for Australian female entrepreneurs, run by Mira Halloway and focuses on empowerment of women and equal opportunity advocacy.</p></div></article>
        <article class="post"><div class="thumb" role="img" aria-label="Video still of a presenter on stage" style="background:linear-gradient(135deg,#c4bcb4,#6e5a50)"></div><div><h3>Ladies in Venture Testimonial Video</h3><div class="date">Mira Halloway, March 6, 2013</div><p>Ladies in Venture (LV) is the No 1 community for Australian female entrepreneurs, run by Mira Halloway and focuses on empowerment of women and equal opportunity advocacy.</p></div></article>
      </section>
      <div class="more"><span>View more Videos</span></div>

      <div class="ad-banner">ClearSkin Board <small>Click Here!</small></div>

      <div class="section-bar">Featured Articles</div>
      <section class="articles">
        <article class="post"><div class="thumb" role="img" aria-label="Photo of a seminar audience" style="background:linear-gradient(135deg,#4a4f58,#9c8f84)"></div><div><h3>Ladies in Venture Testimonial Video</h3><p>Ladies in Venture (LV) is the No 1 community for Australian female entrepreneurs, run by Mira Halloway and focuses on empowerment of women and equal opportunity advocacy female entrepreneurs, run by Mira Halloway and focuses on empowerment of women and equal opportunity advocacy.</p></div></article>
        <article class="post"><div class="thumb" role="img" aria-label="Photo of women at a networking lunch" style="background:linear-gradient(135deg,#8a7262,#d2bfae)"></div><div><h3>Ladies in Venture Testimonial Video</h3><p>Ladies in Venture (LV) is the No 1 community for Australian female entrepreneurs, run by Mira Halloway and focuses on empowerment of women and equal opportunity advocacy female entrepreneurs, run by Mira Halloway and focuses on empowerment of women and equal opportunity advocacy.</p></div></article>
        <article class="post"><div class="thumb" role="img" aria-label="Photo of a group of members" style="background:linear-gradient(135deg,#6b3b3e,#c79a8e)"></div><div><h3>Ladies in Venture Testimonial Video</h3><p>Ladies in Venture (LV) is the No 1 community for Australian female entrepreneurs, run by Mira Halloway and focuses on empowerment of women and equal opportunity advocacy female entrepreneurs, run by Mira Halloway and focuses on empowerment of women and equal opportunity advocacy.</p></div></article>
        <article class="post"><div class="thumb" role="img" aria-label="Photo of women at an evening event" style="background:linear-gradient(135deg,#3f342f,#a08574)"></div><div><h3>Ladies in Venture Testimonial Video</h3><p>Ladies in Venture (LV) is the No 1 community for Australian female entrepreneurs, run by Mira Halloway and focuses on empowerment of women and equal opportunity advocacy female entrepreneurs, run by Mira Halloway and focuses on empowerment of women and equal opportunity advocacy.</p></div></article>
        <article class="post"><div class="thumb" role="img" aria-label="Photo of a dinner gathering" style="background:linear-gradient(135deg,#5a2e2a,#b87a66)"></div><div><h3>Ladies in Venture Testimonial Video</h3><p>Ladies in Venture (LV) is the No 1 community for Australian female entrepreneurs, run by Mira Halloway and focuses on empowerment of women and equal opportunity advocacy female entrepreneurs, run by Mira Halloway and focuses on empowerment of women and equal opportunity advocacy.</p></div></article>
        <article class="post"><div class="thumb" role="img" aria-label="Photo of members posing together" style="background:linear-gradient(135deg,#cfc6bd,#7d6658)"></div><div><h3>Ladies in Venture Testimonial Video</h3><p>Ladies in Venture (LV) is the No 1 community for Australian female entrepreneurs, run by Mira Halloway and focuses on empowerment of women and equal opportunity advocacy female entrepreneurs, run by Mira Halloway and focuses on empowerment of women and equal opportunity advocacy.</p></div></article>
        <article class="post"><div class="thumb" role="img" aria-label="Photo of a conference room" style="background:linear-gradient(135deg,#4c3a30,#b09070)"></div><div><h3>Ladies in Venture Testimonial Video</h3><p>Ladies in Venture (LV) is the No 1 community for Australian female entrepreneurs, run by Mira Halloway and focuses on empowerment of women and equal opportunity advocacy female entrepreneurs, run by Mira Halloway and focuses on empowerment of women and equal opportunity advocacy.</p></div></article>
        <article class="post"><div class="thumb" role="img" aria-label="Photo of a speaker at a lectern" style="background:linear-gradient(135deg,#2b2523,#7d6a5e)"></div><div><h3>Ladies in Venture Testimonial Video</h3><p>Ladies in Venture (LV) is the No 1 community for Australian female entrepreneurs, run by Mira Halloway and focuses on empowerment of women and equal opportunity advocacy female entrepreneurs, run by Mira Halloway and focuses on empowerment of women and equal opportunity advocacy.</p></div></article>
      </section>
      <div class="more"><span>View more Articles</span></div>

      <section class="feed">
        <div class="feed-head"><i></i><div>Ladies in Venture<br><span class="like">Like</span></div></div>
        <div class="feed-photo" role="img" aria-label="Shared photo in the news feed"></div>
        <div class="feed-meta">November 28 at 1:09pm</div>
        <div class="feed-head"><i></i><div>Ladies in Venture</div></div>
        <p>Are you having a gorgeous Thursday? Share your biggest achievement of the week with us below. We'd love to hear about it!</p>
        <div class="feed-quote" role="img" aria-label="Shared quote image"></div>
        <div class="feed-fans">2,045 people like <b>Ladies in Venture</b>.</div>
        <div class="fan-grid" role="img" aria-label="Grid of fan profile photos"></div>
        <div class="feed-foot">Facenook social plugin</div>
      </section>
    </main>

    <aside class="side">
      <div class="side-label">Search for:</div>
      <div class="search"><div class="field"></div><div class="btn">Search</div></div>

      <section class="newsletter">
        <h4>Sign up for our newsletter!</h4>
        <div class="field">Name</div>
        <div class="field">Email</div>
        <div class="signup">Signup</div>
      </section>

      <section class="widget login">
        <h4>Log in to our website!</h4>
        <div class="btn-row"><span>Sign</span><span>Login</span></div>
        <p>Or connect with your Facenook Account</p>
        <span class="fb-connect">Connect with Facenook</span>
      </section>

      <section class="widget poll">
        <h4>Question of the week:</h4>
        <div class="q">Are You Selling Overseas?</div>
        <label><i></i>Yes, in fact most of my sales come from overseas</label>
        <label><i></i>No, I don't and not planning to</label>
        <label><i></i>Yes, I can say I have made a few sales overseas</label>
        <label><i></i>No I don't, but considering entering overseas markets</label>
        <div class="vote">Vote</div>
        <div class="poll-btns"><span>View Results</span><span>Polls Archive</span></div>
      </section>

      <div class="side-ad" role="img" aria-label="Advertisement for chewing gum"><b>MAKE MONEY CHEWING GUM!</b><span>Chewmark Gum Co</span></div>

      <section class="widget events">
        <h4>Upcoming Events</h4>
        <div class="event-title title">The energy and space quite chaotic</div>
        <div class="event"><div class="pic" role="img" aria-label="Event photo"></div><p>It is quite a common occurrence for me to go into people's business and find the energy.</p></div>
        <div class="title">The energy and space quite chaotic</div>
        <div class="event"><div class="pic" role="img" aria-label="Event photo"></div><p>It is quite a common occurrence for me to go into people's business and find the energy.</p></div>
        <div class="title">The energy and space quite chaotic</div>
        <div class="event"><div class="pic" role="img" aria-label="Event photo"></div><p>It is quite a common occurrence for me to go into people's business and find the energy.</p></div>
        <div class="more"><span>View more Events</span></div>
      </section>

      <section class="list">
        <h4>RECENT ACTIVITIES</h4>
        <ul><li>2013-11 Melbourne Meetup</li><li>Cleansing the Workspace</li><li>Little Known Publicity Secret Revealed</li><li>Migrant entrepreneurs overcome barriers to starting</li><li>Get Your Money Running</li></ul>
      </section>

      <section class="list archives">
        <h4>ARCHIVES</h4>
        <ul><li>November 2013</li><li>October 2013</li><li>September 2013</li><li>August 2013</li><li>July 2013</li><li>June 2013</li><li>May 2013</li><li>April 2013</li><li>March 2013</li><li>February 2013</li><li>January 2013</li><li>December 2012</li><li>November 2012</li><li>October 2012</li><li>September 2012</li><li>August 2012</li><li>July 2012</li><li>June 2012</li><li>May 2012</li><li>April 2012</li><li>March 2012</li><li>February 2012</li><li>January 2012</li><li>December 2011</li><li>November 2011</li></ul>
      </section>

      <section class="list">
        <h4>CATEGORIES</h4>
        <ul><li>Article (48)</li><li>Empowerment of Women (2)</li><li>Featured Article (8)</li><li>Featured Video (3)</li><li>female empowerment (3)</li><li>Gallery (13)</li><li>Guest Blog (6)</li><li>Interview (5)</li><li>News (7)</li><li>Video (7)</li><li>Video Interview (25)</li></ul>
      </section>

      <div class="ad2" role="img" aria-label="Advertisement for a diabetes learning resource"><b>SugarWise<br>A Great Resource for Learning About Diabetes</b><span>Insulin Pumps</span></div>

      <section class="list">
        <h4>RECENT COMMENTS</h4>
        <ul><li>Tessa Brandt on Community Support</li><li>Jo Whitcombe on Migrant entrepreneurs overcome barriers to starting up businesses in Australia</li><li>Tessa Brandt on Community Support</li><li>Jo Whitcombe on Migrant entrepreneurs overcome barriers</li><li>Tessa Brandt on Community Support</li></ul>
      </section>
    </aside>
  </div>

  <footer class="footer">
    <div>Copyright © 2013 Ladies in Venture. All rights reserved.</div>
    <div class="social"><span><i></i>Chirplet</span><span><i></i>Facenook</span><span><i></i>Workcircle</span><span><i></i>Pinboardly</span><span><i></i>Feed</span></div>
  </footer>
</div>
</body>
</html>
```